Business card - Harbourline Stoneworks

Design a business card utilizing the given logo.
colors we like: Black, greys, Teal, blues.
Tri color card, horizontal orientation likely
Logo and name likely best on top.
Info on card:

Dennis Farrowby
#5 - 4180 Maple Ridge Blvd.
Surrey, B.C. V3K 2R9

778.555.0193
dennisfarrowby@brellnet.ca

Slogan: "Building Dreams"

We are a construction company that specializes in new home construction on the West coast of BC Canada. Open Concepts designs of high end homes.

```html
<!DOCTYPE html>
<html lang="en">
<head>
<meta charset="utf-8">
<title>Harbourline Stoneworks – Business Card</title>
<link rel="stylesheet" href="https://fonts.googleapis.com/css2?family=Amaranth:wght@700&family=Andika:wght@700&display=swap">
<style>
  :root {
    --card-top: #ffffff;
    --card-bottom: #a9adae;
    --band: #4fe3f6;
    --edge-shadow: rgba(0, 0, 0, 0.55);
    --name-ink: #1c262c;
    --name-deep: #000000;
    --phone-grey: #b8bcbd;
    --text-outline: #3a3a3a;
    --email-blue: #0e4a6b;
    --slogan-teal: #0b7f8e;
    --address-light: #e9ecec;
    --logo-ink: #111111;
    --logo-disc: #ffffff;
  }
  html, body {
    margin: 0;
    padding: 0;
    width: 1200px;
    height: 702px;
    overflow: hidden;
    background: #ffffff;
  }
  .card {
    position: relative;
    width: 1200px;
    height: 702px;
    overflow: hidden;
    font-family: "Andika", "Trebuchet MS", sans-serif;
    font-weight: 700;
  }
  .card__backdrop {
    position: absolute;
    inset: 0;
  }
  .logo-disc {
    position: absolute;
    left: 103px;
    top: 96px;
    width: 276px;
    height: 276px;
    border-radius: 50%;
    background: var(--logo-disc);
    box-shadow: inset 6px 8px 18px rgba(0,0,0,0.55), 2px 3px 4px rgba(255,255,255,0.8);
    display: flex;
    align-items: center;
    justify-content: center;
  }
  .logo-disc__mark {
    display: flex;
    align-items: center;
    gap: 10px;
    transform: rotate(-7deg);
  }
  .logo-disc__dot {
    width: 30px;
    height: 30px;
    border-radius: 50%;
    background: var(--logo-ink);
    flex: none;
  }
  .logo-disc__name {
    color: var(--logo-ink);
    font-family: "Andika", "Trebuchet MS", sans-serif;
    font-weight: 700;
    font-size: 24px;
    line-height: 1.05;
    letter-spacing: 1px;
    text-transform: uppercase;
  }
  .contact-name {
    position: absolute;
    left: 458px;
    top: 56px;
    width: 686px;
    margin: 0;
    text-align: center;
    font-family: "Amaranth", "Trebuchet MS", sans-serif;
    font-weight: 700;
    font-size: 70px;
    letter-spacing: 4px;
    text-transform: uppercase;
    white-space: nowrap;
    color: var(--name-ink);
    text-shadow: 0 -2px 0 var(--name-deep), 3px 4px 3px rgba(0,0,0,0.35);
  }
  .contact-phone {
    position: absolute;
    left: 458px;
    top: 144px;
    width: 686px;
    margin: 0;
    text-align: center;
    font-size: 60px;
    letter-spacing: 5px;
    white-space: nowrap;
    color: var(--phone-grey);
    text-shadow: -1px -1px 0 var(--text-outline), 1px 1px 0 var(--text-outline), 3px 4px 3px rgba(0,0,0,0.45);
  }
  .slogan {
    position: absolute;
    left: 458px;
    top: 262px;
    width: 686px;
    margin: 0;
    text-align: center;
    font-size: 40px;
    letter-spacing: 4px;
    white-space: nowrap;
    color: var(--slogan-teal);
    text-shadow: 2px 3px 2px rgba(0,0,0,0.3);
  }
  .contact-email {
    position: absolute;
    left: 300px;
    top: 474px;
    width: 600px;
    margin: 0;
    text-align: center;
    font-size: 35px;
    letter-spacing: 2px;
    white-space: nowrap;
    color: var(--email-blue);
    text-shadow: 0 -1px 0 var(--name-deep), 2px 3px 2px rgba(0,0,0,0.35);
  }
  .contact-address {
    position: absolute;
    left: 80px;
    top: 560px;
    width: 1000px;
    margin: 0;
    text-align: center;
    font-style: normal;
    font-size: 52px;
    line-height: 56px;
    letter-spacing: 4px;
    white-space: nowrap;
    color: var(--address-light);
    text-shadow: 0 -1px 0 #555, 3px 4px 3px rgba(0,0,0,0.55);
  }
</style>
</head>
<body>
<div class="card">
  <svg class="card__backdrop" width="1200" height="702" viewBox="0 0 1200 702" aria-hidden="true">
    <defs>
      <linearGradient id="panel-fade" x1="0" y1="0" x2="0" y2="1">
        <stop offset="0" stop-color="#ffffff"/>
        <stop offset="1" stop-color="#a9adae"/>
      </linearGradient>
      <filter id="edge-blur" x="-5%" y="-20%" width="110%" height="140%">
        <feGaussianBlur stdDeviation="5"/>
      </filter>
    </defs>
    <rect class="band" width="1200" height="702" fill="#4fe3f6"/>
    <path class="panel-shadow" d="M0 0 H1200 V430 Q600 660 0 430 Z" fill="rgba(0,0,0,0.55)" filter="url(#edge-blur)" transform="translate(0 6)"/>
    <path class="panel" d="M0 0 H1200 V425 Q600 655 0 425 Z" fill="url(#panel-fade)"/>
  </svg>

  <div class="logo-disc">
    <div class="logo-disc__mark">
      <span class="logo-disc__dot"></span>
      <span class="logo-disc__name">Harbourline<br>Stoneworks</span>
    </div>
  </div>

  <h1 class="contact-name">Dennis Farrowby</h1>
  <p class="contact-phone">778.555.0193</p>
  <p class="slogan">Building Dreams</p>
  <p class="contact-email">dennisfarrowby@brellnet.ca</p>
  <address class="contact-address">#5 - 4180 Maple Ridge Blvd.<br>Surrey, B.C. V3K 2R9</address>
</div>
</body>
</html>
```